依頼詳細
★重視する点
60歳~70歳の社長が読むものです。
商品も50万円以上のコンサルティングなので、
信頼感、安心感を与える雰囲気を重視します。
また、高級感のあるイメージも重要です。

★ページ構成について
表面 キャッチ
中面 スキームの説明、Q&A
裏面 報酬、お問合せ先

内容を詰めることができれば、
A4裏表の1枚でもOKです。
(むしろ、そうできればベストです)

★文章の修正について
必要があれば文章やタイトルの修正もOKです。
目的は、
「このような方法があるなら、もっと話しを聞いてみたい」
と思わせることです。
そのように思わせるものであれば、
タイトルや文章の修正も歓迎します。

★お問合せの部分について
数名でこのパンフを共同利用する予定です。
ですから、お問合せの部分は
各自の住所と会社名、電話番号、メールアドレスなどが
入りますので、そのようなスペースを空けておいてください。

★利用用途
このパンフレットは、
問合せがあった人に、最初の相談の時、お渡しします。
またセミナーなど開催したときに、資料としてお渡しします。

★納品形式について
イラストレーターV14で開ける形式でお願いいたします。
また、JpegやPNGもお願いします。
サイズ
A4
ページ数
4ページ
希望イメージ
シンプル 複雑
単色 カラフル
暗い 明るい
日常 高級
遊び心 厳粛
未来的 伝統的
女性的 男性的
希望する色
茶系、グレー系
納品ファイル
• 高解像度JPG (.jpg)
• イラストレーター形式 (.ai)
• PNG形式 (.png)
補足説明
・表面、中面、裏面のラフ案をご提案ください。
こちらの希望するイメージに近い提案を1つ選択させて頂きます。

・希望に近づけるために、修正要望を個別にさせていただくこともあります。
コンペ方式のため、修正後に当選されない場合も、どうかご了承ください。
参加報酬は4件用意していますので、
なるべくそちらで対応するようにいたします。

・今後も同様なものを作成する予定です。
依頼は今回だけではなく、こちらの求める条件に合えば
継続して依頼したいと思います。

・疑問点などございましたらお気軽にご質問ください。
早速に1件のご提案があり、大変ありがとうございます。
さすがプロの方のデザインはすばらしく、
これからの提案もとても期待しております。

★お願い スキームの図解もデザインに盛り込んでください

原案に、自社株信託のスキームの図解がありますが、
できれば、パンフレットにも図解を盛り込んで
いただけないでしょうか?
もちろん、原案のスキームの図を参考に
あなたのイメージするようにデザインし直していただきたいです。

原案がワードで作成したため、マクロウィルスなどご心配の方も
いらっしゃると思いますので、原案のPDFを添付します。
また、スキームの図のPNGも添付します。
図はMSのVisioというソフトで作っております。
開ける人は少ないでしょうが、そのファイルも添付します。
■ 選んだ理由

ビジネスというジャングルを駆け巡る獅子(社長)が
寂しげな目で「引退するか」という表紙は、
提案の中で、圧倒的でした。

また、多くの提案をいただいて、気づいたのですが、
老夫婦だと保険の勧誘、引退をイメージする物だと
投資信託などの金融商品の勧誘のような印象を与えることがわかり、
ライオンの表紙はそのような印象も与えないので、
当選とさせていただきました。

■ 提案者全員のお礼・コメント

多くの方からご応募いただき、誠にありがとうございました。
どの提案も、とても私のような素人ではできない
優れたデザインだったと思います。
さすがプロの仕事を見せていただきました。
また、今後も提案をお願いすると思いますが、
そのときも、よろしくお願いいたします。

この度は大変ありがとうございました。

```html
<!DOCTYPE html>
<html lang="ja">
<head>
<meta charset="utf-8">
<title>自社株信託のご案内</title>
<link rel="stylesheet" href="https://fonts.googleapis.com/css2?family=Noto+Sans+JP:wght@400;700;900&family=Noto+Serif+JP:wght@500;700;900&display=swap">
<style>
:root{
  --brown-deep:#3b2414;
  --brown:#5a3620;
  --brown-mid:#8a5a34;
  --tan:#d9c3a2;
  --tan-light:#efe3cf;
  --cream:#f8f1e5;
  --paper:#fbf7ef;
  --orange:#c96a1b;
  --ink:#3a2a1e;
  --white:#ffffff;
}
*{margin:0;padding:0;box-sizing:border-box}
html,body{width:849px;height:1200px;overflow:hidden;background:var(--white)}
.brochure{position:relative;width:849px;height:1200px;background:var(--paper);font-family:"Noto Sans JP",sans-serif;color:var(--ink)}
.masthead{position:absolute;left:0;top:0;width:849px;height:152px;background:linear-gradient(180deg,var(--brown) 0%,var(--brown-deep) 100%)}
.masthead__kicker{position:absolute;top:14px;left:0;width:100%;text-align:center;font-family:"Noto Serif JP",serif;font-weight:700;font-size:23px;letter-spacing:3px;color:var(--tan)}
.masthead__rule{position:absolute;top:52px;left:40px;right:40px;height:1px;background:var(--brown-mid)}
.masthead__title{position:absolute;top:60px;left:0;width:100%;text-align:center;font-weight:900;font-size:66px;letter-spacing:4px;color:var(--white)}
.hero{position:absolute;left:0;top:152px;width:849px;height:500px;background:linear-gradient(180deg,#ffffff 0%,var(--tan-light) 55%,var(--tan) 100%)}
.hero__question{position:absolute;left:56px;top:28px;font-family:"Noto Serif JP",serif;font-weight:700;font-size:24px;color:var(--orange);letter-spacing:1px}
.hero__lead{position:absolute;left:56px;top:92px;font-family:"Noto Serif JP",serif;font-weight:700;font-size:41px;line-height:1.55;color:var(--brown-deep);letter-spacing:1px}
.hero__lead .accent{color:var(--orange)}
.hero__photo{position:absolute;left:470px;top:20px;width:340px;height:460px}
.body{position:absolute;left:40px;top:672px;width:769px;height:500px;background:var(--cream);border:1px solid var(--tan);display:flex;gap:30px;padding:26px 28px}
.body__col{flex:1;font-size:12.5px;line-height:1.85}
.body__lead{color:var(--orange);font-weight:700;font-size:14px;line-height:1.7;margin-bottom:10px}
.body__col p{margin-bottom:8px}
.body__list{list-style:none;margin:4px 0 8px}
.body__list li::before{content:"・"}
.callout{border:1.5px solid var(--brown-mid);background:var(--white);padding:12px 14px;margin:12px 0;font-family:"Noto Serif JP",serif;font-weight:700;font-size:15px;line-height:1.6;color:var(--brown)}
</style>
</head>
<body>
<main class="brochure">
  <header class="masthead">
    <p class="masthead__kicker">引退をお考えの経営者さまへ</p>
    <div class="masthead__rule"></div>
    <h1 class="masthead__title">自社株信託のご案内</h1>
  </header>

  <section class="hero">
    <p class="hero__question">お持ちの自社株、どうされますか？</p>
    <p class="hero__lead"><span class="accent">「自社株信託」</span>なら、<br>贈与税をかけずに、<br>会社の株を後継者に<br>渡すことができます。</p>
    <svg class="hero__photo" role="img" aria-label="黒い革張りの重役用オフィスチェアの写真" viewBox="0 0 340 460">
      <defs>
        <radialGradient id="chairTone" cx="50%" cy="45%" r="60%">
          <stop offset="0%" stop-color="#4a4440"/>
          <stop offset="100%" stop-color="#d8c7ad" stop-opacity="0"/>
        </radialGradient>
      </defs>
      <rect width="340" height="460" fill="url(#chairTone)"/>
    </svg>
  </section>

  <section class="body">
    <div class="body__col">
      <p class="body__lead">後継者も決まったし、そろそろ引退したいけど、株の譲渡には多額の税金がかかる…</p>
      <p>会社の株式は、経営者さまの財産の中でも大きな割合を占めることが多く、そのまま後継者へ贈与すると高額な贈与税が発生します。業績が良い会社ほど株の評価額は高くなり、後継者の負担も大きくなります。</p>
      <p>よくあるお悩み</p>
      <ul class="body__list">
        <li>株価が高くて贈与できない</li>
        <li>後継者に買い取る資金がない</li>
        <li>相続で株が分散してしまう</li>
      </ul>
      <p>こうした課題は、早めの対策で大きく変わります。</p>
    </div>
    <div class="body__col">
      <p>ただし、会社の価値を下げてまで株を渡すことは、本来の目的ではありません。大切な会社をそのままの形で次の世代へ託したい。そうお考えの経営者さまにこそ、知っていただきたい方法があります。</p>
      <div class="callout">もし、贈与税もかけずに渡せる方法があるとしたら、一度お話を聞いてみませんか？</div>
      <p>自社株信託を活用すると…</p>
      <ul class="body__list">
        <li>贈与税がかからない</li>
        <li>経営権を確実に移せる</li>
        <li>議決権を後継者に集約できる</li>
        <li>株の分散を防ぐことができる</li>
      </ul>
    </div>
  </section>
</main>
</body>
</html>
```